Soccer Club Site Redesign

We are a suburban youth soccer club in need of a web site redesign. Our current site’s look/feel is outdated and is in need of a more modern look. What we are looking for is a design layout that will accommodate the current functionality we have for the site and give us an updated modern look. The deliverable for this project will be .psd file that can be converted to an html theme file for Wordpress. We will take care of the conversion and handle the html coding/javascript functionality.
Take a look at our current site to get an idea of what we offer and the current layout we have.
http://www.fernwickfootball.org
Our club hosts youth recreational soccer, traveling soccer and two large soccer tournaments during the year. We also sponsor a number of training clinics. Our site serves a couple primary purposes:
1. Parents learn how/where/when to sign up their child for the leagues we offer.
2. Parents learn dates/times of various events the club offers.
3. Other soccer clubs get information on the tournaments we offer, sign up for the tournaments etc.
We do a pretty good job of presenting information about the various events/leagues available and how to sign up for them, but we want to do a better job of presenting a calendar where parents can quickly find dates/times of various events. Ideally, we would like to incorporate a news section (like we currently have), with a calendar and the use of more images on the home page. We understand screen space is limited but would incorporate jquery/javascript widgets to hide/show info and maybe an ‘imagebox’ for the additional images.
Here are a few sites with ideas that we liked:
http://sports.dorrington.edu/ (Look at the Upcoming Events calendar on the page)
http://www.ashvalekickers.com/ (look at the Upcoming Events calendar in the right column and the image box in the main content area)
http://www.plumetfutbol.com/index.php (Like the look and use of images)
http://www.rqkickersclub.com/ (imagebox use)
http://www.lorvanpuckclub.org/ ( hockey website but like the use of crisp header graphics)
http://www.ellisfordpuck.com/ (another hockey site, like the calendar used)
That should give you a pretty good idea of what we are looking for. The new design will need to accommodate the existing functionality of the site. Our logo (which is attached) should be incorporated into the site….otherwise we are open to your design ideas.

```html
<!DOCTYPE html>
<html lang="en">
<head>
<meta charset="utf-8">
<title>Fernwick Soccer Club</title>
<link rel="stylesheet" href="https://fonts.googleapis.com/css2?family=Figtree:wght@300;400;500;600;700;800&display=swap">
<style>
:root{
  --page:#0f120f;
  --grass-dark:#14240f;
  --grass:#2c4a1c;
  --grass-light:#3d6226;
  --nav-bg:#1b1b1b;
  --nav-line:#3a3a3a;
  --blue:#1f9be6;
  --blue-dark:#0b6fb8;
  --red:#c8141b;
  --red-dark:#a50e14;
  --white:#ffffff;
  --ink:#222222;
  --muted:#555555;
  --panel:#1a1d18;
  --thumbs:#56657a;
}
*{box-sizing:border-box;margin:0;padding:0}
html,body{width:1093px;height:1200px;overflow:hidden;background:var(--page)}
body{font-family:"Figtree",sans-serif;color:var(--white)}
.stage{position:absolute;left:0;top:0;width:1200px;height:1318px;transform:scale(.9108);transform-origin:0 0;
  background:
    linear-gradient(180deg,#0c130a 0,#0c130a 70px,#142412 70px,#1a2f14 200px,transparent 200px),
    radial-gradient(ellipse at 50% 420px,var(--grass-light) 0,var(--grass) 35%,var(--grass-dark) 62%,var(--page) 80%);
}
.abs{position:absolute}
.account{top:31px;left:929px;display:flex;gap:11px}
.account a{display:block;height:23px;padding:0 13px;line-height:24px;font-size:12px;color:#eee;text-decoration:none;
  background:linear-gradient(#4a4a4a,#262626);border-radius:3px;box-shadow:0 1px 2px #000}
.brand{left:120px;top:72px;width:144px;height:158px;display:flex;align-items:center;justify-content:center;gap:8px}
.brand .mark{width:14px;height:14px;border-radius:50%;background:var(--white)}
.brand span{font-size:20px;font-weight:800;color:var(--white)}
.welcome{left:300px;width:600px;top:86px;text-align:center}
.welcome .small{font-size:38px;font-weight:300;letter-spacing:1px}
.welcome .big{font-size:48px;font-weight:800;margin-top:4px;letter-spacing:.5px}
.ball{border-radius:50%;background:radial-gradient(circle at 38% 32%,#ffffff 0,#e4e4e4 45%,#8a8a8a 100%)}
.header-ball{left:935px;top:78px;width:142px;height:142px}
.nav{left:120px;top:263px;width:171px;list-style:none}
.nav li{height:28px;margin-bottom:1px;background:linear-gradient(#262626,#111);border:1px solid var(--nav-line);border-radius:2px;
  text-align:center;font-size:13px;line-height:27px;font-weight:500}
.nav li.active{background:linear-gradient(#38b3f5,var(--blue-dark));border-color:#52c0f7}
.slider{left:320px;top:264px;width:760px;height:401px;background:var(--panel);border-radius:3px}
.slide-photo{left:337px;top:279px;width:586px;height:372px;background:linear-gradient(180deg,#7fb0d8 0,#8aa0b8 25%,#3b3646 55%,#2f3e2a 80%,#52703a 100%)}
.caption{left:337px;top:585px;width:586px;height:66px;background:rgba(10,12,10,.78);padding:12px 15px}
.caption h2{font-size:17px;font-weight:600}
.caption p{font-size:11px;margin-top:6px;color:#ddd}
.thumbs{left:922px;top:279px;width:143px;height:372px;background:var(--thumbs)}
.thumb-arrow{left:945px;width:97px;height:14px;background:#2e4f8c;display:flex;align-items:center;justify-content:center}
.thumb{left:933px;width:122px;height:88px;border:3px solid var(--white)}
.thumb.sel{border-color:#3d4cb5}
.panel{background:var(--white);border:2px solid #ccc;border-radius:4px;color:var(--ink)}
.news{left:119px;top:708px;width:573px;height:400px}
.news-head{position:absolute;left:6px;top:6px;right:6px;height:37px;background:linear-gradient(#2a2a2a,#0b0b0b);border-radius:3px;
  display:flex;align-items:center;justify-content:space-between;padding:0 12px;color:var(--white)}
.news-head h2{font-size:18px;font-weight:600}
.news-head a,.events-head a{font-size:12px;color:var(--white);text-decoration:none}
.news-item{position:absolute;left:16px;width:517px;display:flex;gap:10px}
.news-item .pic{width:118px;height:85px;flex:none;border:1px solid #999}
.news-item h3{font-size:13px;font-weight:400;line-height:17px;color:#222}
.news-item p{font-size:10px;color:#444;margin-top:3px}
.more{display:inline-block;margin-top:6px;background:var(--red);color:var(--white);font-size:9px;padding:2px 7px;text-decoration:none}
.rule{position:absolute;left:15px;width:517px;height:2px;background:#ddd}
.scroll{position:absolute;left:548px;top:58px;width:8px;height:330px;border:1px solid #bbb;border-radius:4px}
.scroll i{position:absolute;left:-1px;top:66px;width:8px;height:16px;border-radius:4px;background:var(--blue-dark)}
.events{left:717px;top:708px;width:365px;height:400px}
.events-head{position:absolute;left:0;top:0;right:0;height:48px;background:linear-gradient(#d8242a,var(--red-dark));
  display:flex;align-items:center;justify-content:space-between;padding:0 16px 0 15px;color:var(--white)}
.events-head h2{font-size:21px;font-weight:600}
.event{position:absolute;left:16px;width:330px;display:flex;gap:14px}
.date{width:38px;height:36px;flex:none;border:1px solid #ccc;text-align:center}
.date b{display:block;background:var(--red);color:var(--white);font-size:9px;line-height:15px;font-weight:600}
.date span{display:block;font-size:13px;font-weight:600;line-height:19px}
.event p{font-size:13px;line-height:17px;color:#333}
.event strong{font-weight:600;color:#222}
.banner{left:120px;top:1148px;width:694px;height:98px;border-radius:4px;background:linear-gradient(90deg,#0d4ea8,#1b70cc 40%,#1554b0 70%,#0a3c8f)}
.banner-ball{left:122px;top:1149px;width:94px;height:94px}
.banner h2{position:absolute;left:120px;top:28px;font-size:32px;font-weight:700}
.register{position:absolute;left:493px;top:22px;width:177px;height:52px;border-radius:6px;background:linear-gradient(#e4262c,var(--red-dark));
  box-shadow:0 0 0 2px #ff4b4b inset;font-size:19px;font-weight:700;text-align:center;line-height:52px}
.sponsors{left:837px;top:1148px;width:243px;height:99px;background:var(--white);border-radius:4px;display:flex;align-items:center;justify-content:space-around;color:#111}
.sponsor{display:flex;align-items:center;gap:6px;font-size:14px;font-weight:700}
.sponsor i{width:14px;height:14px;background:#1b4fa0}
.sponsor i.round{border-radius:50%;background:#111}
.copyright{left:0;width:1193px;top:1275px;text-align:center;font-size:11px;color:#ddd}
</style>
</head>
<body>
<div class="stage">
  <div class="abs account"><a href="#">LOG IN</a><a href="#">SIGN UP</a></div>

  <div class="abs brand"><i class="mark"></i><span>FERNWICK</span></div>
  <div class="abs welcome">
    <div class="small">WELCOME TO THE</div>
    <div class="big">FERNWICK SOCCER CLUB</div>
  </div>
  <div class="abs ball header-ball" role="img" aria-label="Soccer ball"></div>

  <ul class="abs nav">
    <li class="active">HOME</li><li>ABOUT US</li><li>FORMS</li><li>CALENDAR</li><li>TRAVELING</li>
    <li>RECREATIONAL</li><li>TOURNAMENTS</li><li>REFEREES</li><li>FIELD MAPS</li><li>TEAM MANAGERS</li>
    <li>VOLUNTEERS</li><li>CONTACT US</li><li>SPONSORS</li><li>LINKS</li>
  </ul>

  <div class="abs slider"></div>
  <div class="abs slide-photo" role="img" aria-label="Team photo of players with medals and coach on a sunny field"></div>
  <div class="abs caption">
    <h2>LOREM IPSUM SIT AMET</h2>
    <p>Lorem ipsum dolor sit amet, consectetur adipiscing elit. Donec euismod sodales est, eget semper magna.</p>
  </div>
  <div class="abs thumbs"></div>
  <div class="abs thumb-arrow" style="top:288px"><svg width="12" height="8" viewBox="0 0 12 8"><path d="M1 7 6 2l5 5" fill="none" stroke="#fff" stroke-width="2"/></svg></div>
  <div class="abs thumb" style="top:318px;background:linear-gradient(#6b8a5a,#4b8a2e)" role="img" aria-label="Match action photo"></div>
  <div class="abs thumb sel" style="top:421px;background:linear-gradient(#9bb7d6,#2c3f8a 60%,#5e8c3a)" role="img" aria-label="Team group photo"></div>
  <div class="abs thumb" style="top:524px;background:linear-gradient(#b9c6cf,#2a5ab5 60%,#5f8c3c)" role="img" aria-label="Team group photo in blue kits"></div>
  <div class="abs thumb-arrow" style="top:628px"><svg width="12" height="8" viewBox="0 0 12 8"><path d="M1 1l5 5 5-5" fill="none" stroke="#fff" stroke-width="2"/></svg></div>

  <section class="abs panel news">
    <div class="news-head"><h2>NEWS</h2><a href="#">VIEW ALL NEWS</a></div>
    <article class="news-item" style="top:63px">
      <div class="pic" role="img" aria-label="School teams celebrating" style="background:linear-gradient(#7a8a6a,#3d5a9a 60%,#4a6e30)"></div>
      <div><h3>FERNWICK HIGH SCHOOL BOYS AND GIRLS TEAMS BOTH WIN STATE QUARTERS TO MOVE TO THE FINAL 4 AT THE RIVERDOME!</h3><a class="more" href="#">READ MORE</a></div>
    </article>
    <div class="rule" style="top:163px"></div>
    <article class="news-item" style="top:178px">
      <div class="pic" role="img" aria-label="Champion team group photo" style="background:linear-gradient(#8a6a4a,#6a3a30 50%,#3a4a7a)"></div>
      <div><h3>NLYSA FALL STATE CHAMPION AND FALL LEAGUE CHAM-PIONS</h3><p>Lorem ipsum dolor sit amet, consectetur adipiscing elit....</p><a class="more" href="#">READ MORE</a></div>
    </article>
    <div class="rule" style="top:277px"></div>
    <article class="news-item" style="top:293px">
      <div class="pic" role="img" aria-label="Travel team in red kits" style="background:linear-gradient(#c9ccd0,#a8232a 55%,#55703a)"></div>
      <div><h3>SUMMER TRAVEL 2013 - ROSTER SPOTS OPEN: U11 AND U12 GIRLS C3, U13 BOYS C3 AND U14 GIRLS C2</h3><p>Lorem ipsum dolor sit amet, consectetur adipiscing elit....</p><a class="more" href="#">READ MORE</a></div>
    </article>
    <div class="scroll"><i></i></div>
  </section>

  <section class="abs panel events">
    <div class="events-head"><h2>UPCOMING EVENTS</h2><a href="#">VIEW ALL EVENTS</a></div>
    <div class="event" style="top:63px"><div class="date"><b>NOV</b><span>02</span></div><p><strong>Calder North Executive Committee Election applications due</strong> - ( 1 pm - 4 pm )</p></div>
    <div class="event" style="top:119px"><div class="date"><b>NOV</b><span>05</span></div><p><strong>Tournament Weekend</strong> - ( 12 pm - 5 pm )<br>(05/09/2012 - 06/09/2012)</p></div>
    <div class="event" style="top:174px"><div class="date"><b>NOV</b><span>09</span></div><p><strong>Tournament Weekend</strong> - ( 1 pm - 4 pm )<br>(09/09/2012 - 10/09/2012)</p></div>
    <div class="event" style="top:231px"><div class="date"><b>NOV</b><span>12</span></div><p><strong>District Commissioner Meeting</strong><br>- ( 11 am - 12 pm )</p></div>
    <div class="event" style="top:286px"><div class="date"><b>NOV</b><span>15</span></div><p><strong>Board of Directors Meeting- Dec. '12</strong><br>- ( 1 pm - 2 pm )</p></div>
    <div class="event" style="top:342px"><div class="date"><b>NOV</b><span>19</span></div><p><strong>U12-U14 Founders' Cup Preliminary Round Games</strong> - ( 1 pm - 5 pm )</p></div>
  </section>

  <div class="abs banner">
    <h2>2013 TRAVEL SOCCER</h2>
    <div class="register">REGISTER HERE</div>
  </div>
  <div class="abs ball banner-ball" role="img" aria-label="Soccer ball"></div>

  <div class="abs sponsors">
    <div class="sponsor"><i></i>NLYSA</div>
    <div class="sponsor"><i class="round"></i>Stridewell</div>
  </div>

  <div class="abs copyright">COPYRIGHT © FERNWICK SOCCER CLUB 2012</div>
</div>
</body>
</html>
```